Marrowfield Contracting Business Cards

Front of card:

Full Logo
Name
Address
Office Phone
Cell Phone
Email
Website

Back:
Logo Mark in background
List and markets and services performed

```html
<!DOCTYPE html>
<html lang="en">
<head>
<meta charset="utf-8">
<title>Marrowfield Contracting Business Cards</title>
<link href="https://fonts.googleapis.com/css2?family=Exo+2:wght@400;500;600&display=swap" rel="stylesheet">
<style>
  :root {
    --canvas: #f4f4f4;
    --card-red: #d21c1c;
    --ink: #ffffff;
    --ink-soft: rgba(255,255,255,0.75);
    --shadow: rgba(0,0,0,0.28);
  }
  * { margin: 0; padding: 0; box-sizing: border-box; }
  html, body { width: 1200px; height: 1200px; overflow: hidden; }
  body {
    background: var(--canvas);
    font-family: "Exo 2", "Segoe UI", sans-serif;
    color: var(--ink);
    display: flex;
    flex-direction: column;
    align-items: center;
    justify-content: center;
    gap: 34px;
  }
  .card {
    position: relative;
    width: 960px;
    height: 548px;
    background: var(--card-red);
    box-shadow: 10px 12px 22px var(--shadow);
  }

  /* brand lockup */
  .brand { position: absolute; display: flex; align-items: center; gap: 12px; }
  .brand-mark {
    border: 5px solid var(--ink);
    border-radius: 50%;
    flex: none;
  }
  .brand-name {
    font-weight: 600;
    text-transform: uppercase;
    line-height: 1.05;
    color: var(--ink);
  }
  .brand-name .llc { display: block; text-align: right; }

  .card-front .brand { top: 78px; right: 70px; }
  .card-front .brand-mark { width: 70px; height: 70px; }
  .card-front .brand-name { font-size: 21px; letter-spacing: 0.5px; }
  .card-front .brand-name .llc { font-size: 11px; }

  .holder { position: absolute; left: 52px; top: 290px; }
  .holder-name { font-size: 50px; font-weight: 500; letter-spacing: 0.5px; line-height: 1; }
  .holder-role { font-size: 18px; font-weight: 400; margin-top: 8px; }

  .contact-row {
    position: absolute;
    left: 52px;
    right: 60px;
    top: 440px;
    display: flex;
    align-items: flex-start;
    font-size: 17px;
    font-weight: 400;
  }
  .contact-group { display: flex; flex-direction: column; gap: 10px; }
  .contact-group.phones { width: 255px; }
  .contact-group.web { width: 320px; }
  .contact-divider {
    width: 1px; height: 30px;
    background: var(--ink-soft);
    margin: 6px 32px 0 0;
  }
  .contact-line { display: flex; align-items: flex-start; gap: 10px; line-height: 22px; }
  .contact-line .icon { width: 20px; height: 20px; flex: none; margin-top: 1px; }
  .contact-line .indent { margin-left: 30px; }

  /* back */
  .card-back .brand {
    left: 0; right: 0; top: 130px;
    flex-direction: column;
    gap: 16px;
  }
  .card-back .brand-mark { width: 132px; height: 132px; border-width: 7px; }
  .card-back .brand-name { font-size: 34px; text-align: center; }
  .card-back .brand-name .llc { font-size: 14px; }
  .services {
    position: absolute;
    left: 52px; right: 52px; top: 456px;
    display: flex; align-items: center; gap: 14px;
    font-size: 14px; font-weight: 500;
  }
  .services-rule { flex: 1; height: 1px; background: var(--ink-soft); }
</style>
</head>
<body>

<section class="card card-front" aria-label="Business card front">
  <div class="brand">
    <span class="brand-mark"></span>
    <div class="brand-name">Marrowfield<br>Contracting<span class="llc">LLC</span></div>
  </div>

  <div class="holder">
    <h1 class="holder-name">Owen Hartley</h1>
    <p class="holder-role">Managing Director</p>
  </div>

  <div class="contact-row">
    <div class="contact-group phones">
      <div class="contact-line">
        <svg class="icon" viewBox="0 0 20 20" aria-hidden="true"><circle cx="10" cy="10" r="10" fill="#fff"/><path d="M7 5.5l1.6 2.4-1 1.1a6 6 0 0 0 3.4 3.4l1.1-1 2.4 1.6-.8 1.6c-3.5.2-7.6-3.9-7.4-7.4z" fill="#d21c1c"/></svg>
        <span>(000)123-4567</span>
      </div>
      <div class="contact-line"><span class="indent">(000)234-5765</span></div>
    </div>
    <span class="contact-divider"></span>
    <div class="contact-group web">
      <div class="contact-line">
        <svg class="icon" viewBox="0 0 20 20" aria-hidden="true"><circle cx="10" cy="10" r="10" fill="#fff"/><rect x="5" y="6.5" width="10" height="7" rx="1" fill="#d21c1c"/><path d="M5.5 7l4.5 3.5L14.5 7" stroke="#fff" stroke-width="1" fill="none"/></svg>
        <span>hello@marrowfieldco.com</span>
      </div>
      <div class="contact-line">
        <svg class="icon" viewBox="0 0 20 20" aria-hidden="true"><circle cx="10" cy="10" r="10" fill="#fff"/><circle cx="10" cy="10" r="5" fill="none" stroke="#d21c1c" stroke-width="1.3"/><path d="M5 10h10M10 5c-2.5 3-2.5 7 0 10M10 5c2.5 3 2.5 7 0 10" stroke="#d21c1c" stroke-width="1.1" fill="none"/></svg>
        <span>www.marrowfieldco.com</span>
      </div>
    </div>
    <span class="contact-divider"></span>
    <div class="contact-group address">
      <div class="contact-line">
        <svg class="icon" viewBox="0 0 20 20" aria-hidden="true"><circle cx="10" cy="10" r="10" fill="#fff"/><path d="M10 4.5a3.8 3.8 0 0 0-3.8 3.8c0 2.8 3.8 7 3.8 7s3.8-4.2 3.8-7A3.8 3.8 0 0 0 10 4.5z" fill="#d21c1c"/><circle cx="10" cy="8.3" r="1.4" fill="#fff"/></svg>
        <span>123 Street Name City Name<br>State, Country, 12345</span>
      </div>
    </div>
  </div>
</section>

<section class="card card-back" aria-label="Business card back">
  <div class="brand">
    <span class="brand-mark"></span>
    <div class="brand-name">Marrowfield<br>Contracting<span class="llc">LLC</span></div>
  </div>
  <div class="services">
    <span class="services-rule"></span>
    <span class="services-text">List and Markets and Services Performed</span>
  </div>
</section>

</body>
</html>
```